Letterhead Design Project for online gaming site

We need a letterhead for a new online gaming company. The site is www.lunorapick.co

The logo is a gold colour and the site is similar in nature. Feel free to take a look at the landing page.

However the designer has free reign to do whatever they like with it.

OTHER CONTENT:

Telephone: 1300 617 385
Email: info@lunorapick.co
Web: www.lunorapick.co

Industry/Entity Type

It Company

```html
<!DOCTYPE html>
<html lang="en">
<head>
<meta charset="utf-8">
<title>LunoraPick.co Letterhead</title>
<link rel="stylesheet" href="https://fonts.googleapis.com/css2?family=Fredoka:wght@600&family=Tinos:wght@400;700&display=swap">
<style>
  :root {
    --backdrop: #d9d9d9;
    --header-dark: #2b241c;
    --header-mid: #3a3024;
    --gold-deep: #c9a21f;
    --gold-mid: #d9b430;
    --gold-light: #e6cb57;
    --gold-text: #f2c21a;
    --nav-outline: #5a4208;
    --silhouette: #b8921c;
    --contact-bg: #2a241d;
    --contact-text: #f4efe6;
  }
  html, body {
    margin: 0;
    padding: 0;
    width: 968px;
    height: 1200px;
    overflow: hidden;
    background: var(--backdrop);
  }
  .letterhead {
    position: absolute;
    left: 34px;
    top: 18px;
    width: 900px;
    height: 1164px;
    overflow: hidden;
    background:
      repeating-linear-gradient(90deg, rgba(255,255,255,0.05) 0 2px, rgba(0,0,0,0.04) 2px 5px, rgba(255,255,255,0.02) 5px 9px),
      linear-gradient(180deg, var(--gold-deep) 0%, var(--gold-mid) 30%, var(--gold-light) 52%, var(--gold-mid) 75%, var(--gold-deep) 100%);
    box-shadow: 0 4px 18px rgba(0,0,0,0.25);
  }
  .masthead {
    position: absolute;
    left: 0; top: 0;
    width: 100%;
    height: 176px;
    background: radial-gradient(ellipse at 50% 30%, var(--header-mid), var(--header-dark) 75%);
    box-shadow: 0 3px 6px rgba(0,0,0,0.35);
  }
  .brand-name {
    position: absolute;
    top: 38px;
    left: 0; right: 0;
    text-align: center;
    font-family: "Fredoka", sans-serif;
    font-weight: 600;
    font-size: 62px;
    line-height: 1;
    color: var(--gold-text);
    letter-spacing: 0.5px;
  }
  .nav {
    position: absolute;
    top: 132px;
    left: 0; right: 0;
    display: flex;
    justify-content: center;
    gap: 28px;
    font-family: "Fredoka", sans-serif;
    font-weight: 600;
    font-size: 29px;
    color: var(--gold-text);
    text-shadow:
      1px 1px 0 var(--nav-outline), -1px -1px 0 var(--nav-outline),
      1px -1px 0 var(--nav-outline), -1px 1px 0 var(--nav-outline);
  }
  .racing-silhouettes {
    position: absolute;
    left: 10px;
    top: 1020px;
    width: 560px;
    height: 130px;
    background: radial-gradient(ellipse at 45% 55%, rgba(168,132,20,0.55), rgba(168,132,20,0) 70%);
  }
  .footer-shade {
    position: absolute;
    left: 0; bottom: 0;
    width: 100%;
    height: 70px;
    background: linear-gradient(180deg, rgba(40,30,10,0) 0%, rgba(40,30,10,0.85) 100%);
  }
  .contact-panel {
    position: absolute;
    left: 600px;
    top: 1020px;
    width: 300px;
    height: 131px;
    background: var(--contact-bg);
    border-radius: 12px 0 0 12px;
    box-sizing: border-box;
    padding: 18px 34px 0 0;
    text-align: right;
    font-family: "Tinos", serif;
    font-size: 20px;
    line-height: 33px;
    color: var(--contact-text);
  }
  .contact-panel b { font-weight: 700; }
</style>
</head>
<body>
  <div class="letterhead">
    <header class="masthead">
      <div class="brand-name">LunoraPick.co</div>
      <nav class="nav">
        <span>Thoroughbred</span>
        <span>Harness</span>
        <span>Greyhound</span>
        <span>Sport &amp; Lay Betting</span>
      </nav>
    </header>

    <div class="racing-silhouettes" role="img" aria-label="Faint silhouettes of a harness racer, a galloping racehorse with jockey and running greyhounds"></div>
    <div class="footer-shade"></div>

    <address class="contact-panel" style="font-style:normal">
      <div><b>Tel:</b> 1300 617 385</div>
      <div><b>Email:</b> info@lunorapick.co</div>
      <div><b>Web:</b> www.lunorapick.co</div>
    </address>
  </div>
</body>
</html>
```